Re-design of current business cards

We are updating our website with new colors and layout. Would like to re-design our business cards to co-ordinate. See attached pdf with new Brindlecraft website colors. We would also like to combine our 2 brands on the one business card. Attached is the new design for our Brindlecraft website, current business cards, which are one sided, brindlecraft logo in tiff, .ai for fonts. Brindlecraft logo font is Optimum, Quillmarsh website home page image, Quillmarsh brand statics for products which includes the logo for this brand.

Quillmarsh brand will stay the dark gray on the website. See attached statics for product and website home page.
Updates

The business cards will be 2 sided. Brindlecraft Brand on one side and Quillmarsh Brand on the other. The colors for Brindlecraft need to follow the color scheme of the brindlecraft website pdf I uploaded. The colors are a blue, lighter teal blue and white. Quillmarsh needs to follow the dark gray color on files uploaded

Target Market(s)

The trade and consumers

Industry/Entity Type

Home Furnishing

Contact Information for Business Card

We are updating our website with new colors and layout. Would like to re-design our business cards to co-ordinate. We would also like to combine our 2 brands onto 1 2 sided business cards.

Requirements
Must have
• Colors that match our new website, see attached image.
• RGB colors
• navy -#152842
• teal - 98aeb9
• The gray color used for Quillmarsh brands.
• ll logos and fonts should stay the same.

```html
<!DOCTYPE html>
<html lang="en">
<head>
<meta charset="utf-8">
<title>Brindlecraft Business Card</title>
<link rel="stylesheet" href="https://fonts.googleapis.com/css2?family=Source+Sans+3:wght@300;400;700&display=swap">
<style>
  :root {
    --navy: #152842;
    --teal: #98aeb9;
    --white: #ffffff;
  }
  html, body {
    margin: 0;
    padding: 0;
    width: 1200px;
    height: 760px;
    overflow: hidden;
    background: var(--white);
  }
  .card {
    position: relative;
    width: 1200px;
    height: 760px;
    box-sizing: border-box;
    border: 3px solid var(--navy);
    background: var(--white);
    font-family: "Source Sans 3", sans-serif;
    color: var(--navy);
    overflow: hidden;
  }
  .card__panel {
    position: absolute;
    inset: 0;
    width: 1200px;
    height: 760px;
  }
  .card__panel polygon { fill: var(--navy); }
  .person { position: absolute; left: 122px; top: 124px; }
  .person__name {
    margin: 0;
    font-weight: 700;
    font-size: 57px;
    line-height: 1;
    letter-spacing: 2.5px;
    color: var(--teal);
  }
  .person__title {
    margin: 12px 0 0 5px;
    font-weight: 300;
    font-size: 36px;
    line-height: 1;
    letter-spacing: 1px;
    color: var(--teal);
  }
  .brand {
    position: absolute;
    right: 27px;
    top: 118px;
    text-align: right;
    font-weight: 400;
    color: var(--navy);
  }
  .brand__name {
    font-size: 66px;
    line-height: 1;
    letter-spacing: 0;
  }
  .brand__sub {
    font-size: 29px;
    line-height: 1;
    margin-top: 4px;
    letter-spacing: 1.5px;
  }
  .icon { position: absolute; fill: var(--navy); }
  .contact {
    position: absolute;
    font-size: 31px;
    line-height: 1;
    font-weight: 400;
    color: var(--navy);
    white-space: nowrap;
  }
  .contact--email { left: 781px; top: 322px; }
  .contact--address { left: 689px; top: 447px; line-height: 60px; margin-top: -14px; }
  .contact--phone { left: 515px; top: 612px; }
  .contact--fax { left: 902px; top: 615px; }
</style>
</head>
<body>
<div class="card">
  <svg class="card__panel" viewBox="0 0 1200 760" aria-hidden="true">
    <polygon points="0,0 932,0 248,760 0,760"/>
  </svg>

  <div class="person">
    <h1 class="person__name">DANA WHITLOW</h1>
    <p class="person__title">GRAPHIC DIRECTOR</p>
  </div>

  <div class="brand">
    <div class="brand__name">QUILLMARSH</div>
    <div class="brand__sub">by BRINDLECRAFT</div>
  </div>

  <svg class="icon icon--email" style="left:686px;top:310px" width="48" height="36" viewBox="0 0 48 36" aria-hidden="true">
    <rect width="48" height="36"/>
    <polyline points="2,3 24,22 46,3" fill="none" stroke="#ffffff" stroke-width="2.5"/>
  </svg>
  <div class="contact contact--email">DWHIT@BRINDLECRAFT.COM</div>

  <svg class="icon icon--pin" style="left:576px;top:444px" width="38" height="68" viewBox="0 0 38 68" aria-hidden="true">
    <path d="M19 0C8.5 0 0 8.5 0 19c0 13 19 49 19 49s19-36 19-49C38 8.5 29.5 0 19 0zm0 27a8 8 0 1 1 0-16 8 8 0 0 1 0 16z"/>
  </svg>
  <div class="contact contact--address">
    PO BOX 412/1870 FERNWAY RIDGE RD<br>
    MAPLE HOLLOW, VIRGINIA 24099
  </div>

  <svg class="icon icon--phone" style="left:442px;top:596px" width="48" height="54" viewBox="0 0 48 54" aria-hidden="true">
    <path d="M10 1l8 12c1 2 0 4-1 5l-4 3c2 8 8 16 15 20l4-3c2-1 4-1 5 0l10 9c1 1 1 3 0 4l-5 3c-4 2-9 1-13-2C17 43 7 30 3 16 2 11 2 6 5 3l2-2c1-1 2-1 3 0z"/>
  </svg>
  <div class="contact contact--phone">555.210.4837</div>

  <svg class="icon icon--fax" style="left:822px;top:608px" width="48" height="42" viewBox="0 0 48 42" aria-hidden="true">
    <rect x="10" y="0" width="28" height="14"/>
    <path d="M4 16h40a4 4 0 0 1 4 4v18a4 4 0 0 1-4 4H4a4 4 0 0 1-4-4V20a4 4 0 0 1 4-4z"/>
    <rect x="8" y="24" width="32" height="3" fill="#ffffff"/>
  </svg>
  <div class="contact contact--fax">555.210.4912</div>
</div>
</body>
</html>
```